Our brand new and excilting business, ZIPPA things, needs a fresh, vibriant and clean website that is

We need a new website designed to sell our ZIPPA things products to schools and fundraisers. We plan to have around 24 items with great images, add to cart and some really new and cool products. This site needs to be clean, fresh and funky, really clean lines, easy to navigate but look really fun and fresh

Target Market(s)

School fundraising. Kids

Industry/Entity Type

Business

Number of Pages Required

4 page

Colors
add136
fbee3d
fbed22
9bcb3c
f78f20

Requirements
Must have
• Fresh, fun and easy to navigate. Great shopping product page that has images of our products and add to cart
Nice to have
• Flashing image availibility
Should not have
• Must not be old and boring

```html
<!DOCTYPE html>
<html lang="en">
<head>
<meta charset="utf-8">
<title>ZIPPA things – School Fundraising Shop</title>
<link href="https://fonts.googleapis.com/css2?family=Open+Sans:wght@400;600;700;800&family=Kaushan+Script&display=swap" rel="stylesheet">
<style>
:root{
  --orange:#f78f20;
  --yellow:#fbed22;
  --yellow-soft:#fbee3d;
  --green:#9bcb3c;
  --red:#ad1136;
  --red-dark:#7d0c27;
  --page:#2e2e2e;
  --header:#1d1d1d;
  --panel:#1a1a1a;
  --card:#232323;
  --line:#3c3c3c;
  --text:#f2f2f2;
  --muted:#9a9a9a;
}
*{box-sizing:border-box;margin:0;padding:0}
html,body{width:1200px;height:2304px;overflow:hidden}
body{background:var(--page);font-family:'Open Sans',Arial,sans-serif;color:var(--text);position:relative}
.wrap{position:absolute;left:72px;width:1056px}

/* header */
.site-header{position:absolute;top:0;left:0;width:1200px;height:112px;background:var(--header)}
.brand{position:absolute;left:72px;top:34px;font-size:40px;font-weight:800;color:var(--orange);line-height:1;letter-spacing:-1px;white-space:nowrap}
.top-links{position:absolute;right:150px;top:12px;font-size:12px;color:#cfcfcf;white-space:nowrap}
.top-links span{margin:0 6px;color:#666}
.currency{position:absolute;right:72px;top:8px;width:64px;height:24px;background:var(--yellow);color:#222;font-size:12px;font-weight:700;text-align:center;line-height:24px;border-radius:3px}
.search{position:absolute;left:670px;top:52px;width:270px;height:34px;background:#fff;border-radius:3px;font-size:13px;color:#999;line-height:34px;padding-left:12px}
.search svg{position:absolute;right:10px;top:9px}
.cart{position:absolute;right:72px;top:46px;width:160px;height:46px;background:var(--orange);border-radius:3px;padding:5px 8px 0 40px;font-size:12px;font-weight:700;color:#fff;line-height:18px;white-space:nowrap}
.cart svg{position:absolute;left:10px;top:12px}
.cart small{font-weight:400;font-size:11px}

/* navigation */
.main-nav{position:absolute;top:112px;left:0;width:1200px;height:44px;background:linear-gradient(var(--yellow-soft),var(--orange))}
.main-nav ul{list-style:none;display:flex;justify-content:space-between;width:1056px;margin-left:72px;height:44px;align-items:center}
.main-nav li{font-size:13px;font-weight:800;color:#2a2a2a;text-transform:uppercase;letter-spacing:.3px}

/* welcome */
.welcome{top:176px;height:108px;background:var(--panel);border:1px solid var(--line);border-radius:6px}
.badge{position:absolute;top:10px;width:120px;height:88px;border-radius:10px;font-size:13px;font-weight:800;text-align:center;display:flex;align-items:center;justify-content:center;padding:0 10px;line-height:16px}
.badge-guarantee{left:14px;background:var(--orange);color:#fff}
.badge-discount{right:14px;background:var(--green);color:#1e1e1e}
.welcome p{position:absolute;left:170px;right:170px;top:28px;text-align:center;font-size:20px;font-weight:700;line-height:26px}
.welcome p em{color:var(--yellow);font-style:normal}

/* hero */
.hero{top:300px;height:470px;border-radius:6px;overflow:hidden;background:linear-gradient(120deg,#0d0d14 0%,#3a1a4a 35%,#0f3a5a 60%,#541a2a 85%,#111 100%)}
.hero-title{position:absolute;right:80px;top:110px;font-family:'Kaushan Script',cursive;font-size:54px;color:var(--yellow);line-height:60px;text-align:center}
.shop-now{position:absolute;right:250px;top:380px;background:var(--red);color:#fff;font-size:14px;font-weight:800;padding:10px 22px;border-radius:4px;text-transform:uppercase}
.arrow{position:absolute;top:215px;width:40px;height:40px;border-radius:50%;background:rgba(0,0,0,.6);display:flex;align-items:center;justify-content:center}
.arrow.prev{left:12px}.arrow.next{right:12px}
.dots{position:absolute;top:800px;left:0;width:1200px;display:flex;justify-content:center;gap:10px}
.dots i{width:10px;height:10px;border-radius:50%;background:#666;display:block}
.dots i.on{background:var(--orange)}

/* featured */
.ribbon{position:absolute;top:920px;left:500px;width:200px;height:42px;background:var(--red);color:#fff;font-size:16px;font-weight:700;text-align:center;line-height:42px}
.ribbon:before,.ribbon:after{content:"";position:absolute;top:8px;width:30px;height:42px;background:var(--red-dark);z-index:-1}
.ribbon:before{left:-22px}.ribbon:after{right:-22px}
.products{position:absolute;left:160px;width:880px;display:grid;grid-template-columns:repeat(4,208px);gap:16px}
.row-1{top:1005px}.row-2{top:1440px}
.card{height:320px;background:var(--card);border:1px solid var(--line);border-radius:4px;overflow:hidden;position:relative}
.card .photo{height:190px}
.p-ring{background:radial-gradient(circle at 50% 55%,#f78f20,#4a8a1a 55%,#111)}
.p-cup{background:radial-gradient(circle at 50% 55%,#6fd0ff,#1c6a3a 55%,#0a0a0a)}
.p-wind{background:radial-gradient(circle at 60% 50%,#6ad4ff,#5a2a8a 50%,#141a2a)}
.p-foam{background:linear-gradient(135deg,#3a1a6a,#1a7aa0 50%,#e04aa0)}
.card h3{font-size:14px;font-weight:700;text-align:center;margin-top:12px;white-space:nowrap}
.card p{font-size:11px;color:var(--muted);text-align:center;padding:4px 14px;line-height:15px}
.card-foot{position:absolute;bottom:0;left:0;right:0;height:42px;border-top:1px solid var(--line);display:flex;align-items:center;padding-left:10px;gap:6px}
.card-foot .icon{width:26px;height:26px;background:var(--orange);border-radius:3px;display:flex;align-items:center;justify-content:center}
.price{margin-left:auto;height:42px;width:86px;background:var(--green);color:#1e1e1e;font-size:18px;font-weight:800;text-align:center;line-height:42px}

/* perks */
.perks{position:absolute;top:1880px;left:0;width:1200px;height:88px;background:#242424;border-top:1px solid var(--line);border-bottom:1px solid var(--line);display:flex;justify-content:center;gap:120px;align-items:center}
.perk{font-family:'Kaushan Script',cursive;font-size:26px;color:#fff;text-align:center;line-height:26px}
.perk small{display:block;font-family:'Open Sans',sans-serif;font-size:11px;font-weight:700;color:var(--orange);text-transform:uppercase}

/* newsletter */
.newsletter{position:absolute;top:1990px;left:72px;width:1056px;height:48px;display:flex;align-items:center}
.newsletter .label{font-size:12px;font-weight:800;text-transform:uppercase;width:150px;line-height:15px;padding-left:32px;position:relative}
.newsletter .label svg{position:absolute;left:0;top:5px}
.newsletter .field{width:280px;height:32px;background:#fff;border-radius:3px;color:#999;font-size:12px;line-height:32px;padding-left:10px;margin-left:20px}
.newsletter .btn{height:32px;background:var(--orange);font-size:12px;font-weight:800;line-height:32px;padding:0 16px;border-radius:3px;margin-left:8px;text-transform:uppercase;white-space:nowrap}
.social{margin-left:auto;display:flex;align-items:center;gap:8px;font-size:12px;font-weight:800;text-transform:uppercase;white-space:nowrap}
.social i{width:26px;height:26px;border-radius:50%;background:#555;display:block}

/* footer */
.footer-cols{position:absolute;top:2075px;left:72px;width:1056px;display:grid;grid-template-columns:240px 240px 220px 356px}
.footer-cols h4{font-size:13px;font-weight:800;text-transform:uppercase;margin-bottom:10px}
.footer-cols li{list-style:none;font-size:12px;color:var(--muted);line-height:21px}
.pay{display:flex;gap:8px}
.pay i{width:52px;height:32px;border-radius:3px;background:#e9e9e9;display:block}
.copyright{position:absolute;top:2260px;left:0;width:1200px;height:44px;background:var(--header);text-align:center;font-size:11px;color:var(--muted);line-height:44px}
</style>
</head>
<body>

<header class="site-header">
  <div class="brand">ZIPPA things</div>
  <div class="top-links">My Account<span>|</span>Customer Service<span>|</span>0800 555 0142</div>
  <div class="currency">USD</div>
  <div class="search">Search...
    <svg width="16" height="16" viewBox="0 0 16 16"><circle cx="6.5" cy="6.5" r="5" fill="none" stroke="#777" stroke-width="2"/><line x1="10" y1="10" x2="15" y2="15" stroke="#777" stroke-width="2"/></svg>
  </div>
  <div class="cart">
    <svg width="22" height="20" viewBox="0 0 22 20"><path d="M1 2h4l3 11h11l2-8H6" fill="none" stroke="#fff" stroke-width="2"/><circle cx="9" cy="17" r="2" fill="#fff"/><circle cx="17" cy="17" r="2" fill="#fff"/></svg>
    SHOPPING CART<br><small>(0) items $0.00</small>
  </div>
</header>

<nav class="main-nav">
  <ul>
    <li>Glow Sticks</li><li>Light Up Novelties</li><li>Glowing Necklaces</li><li>Glow Bracelets</li><li>Glow Novelties</li><li>Party Supplies</li><li>Wholesale</li>
  </ul>
</nav>

<section class="wrap welcome">
  <div class="badge badge-guarantee">100% Guaranteed replace or refund offered</div>
  <p>Welcome! Buy glow necklaces, glow bracelets,<br><em>glowsticks &amp; MUCH more!</em></p>
  <div class="badge badge-discount">PTA and charity discount available</div>
</section>

<section class="wrap hero" role="img" aria-label="Photo of children wearing colourful light-up noodle hair">
  <div class="hero-title">Crazy Hair<br>Noodle Hair</div>
  <div class="shop-now">Shop Now</div>
  <div class="arrow prev"><svg width="14" height="14" viewBox="0 0 14 14"><path d="M10 1L3 7l7 6" fill="none" stroke="#fff" stroke-width="2.5"/></svg></div>
  <div class="arrow next"><svg width="14" height="14" viewBox="0 0 14 14"><path d="M4 1l7 6-7 6" fill="none" stroke="#fff" stroke-width="2.5"/></svg></div>
</section>
<div class="dots"><i class="on"></i><i></i><i></i></div>

<div class="ribbon">Featured Products</div>

<section class="products row-1">
  <article class="card"><div class="photo p-ring" role="img" aria-label="Flashing animal soft rings"></div><h3>Flashing Animal Soft Rings</h3><p>Soft light-up rings that flash in bright fun colours.</p><div class="card-foot"><span class="icon"><svg width="12" height="12"><path d="M1 6h10M6 1v10" stroke="#fff" stroke-width="2"/></svg></span><span class="icon"><svg width="12" height="12"><path d="M6 11L1 5a3 3 0 0 1 5-3 3 3 0 0 1 5 3z" fill="#fff"/></svg></span><span class="price">£0.89</span></div></article>
  <article class="card"><div class="photo p-cup" role="img" aria-label="Glowing party cups"></div><h3>Glow Cups</h3><p>Light-up cups that glow brightly at any school party.</p><div class="card-foot"><span class="icon"><svg width="12" height="12"><path d="M1 6h10M6 1v10" stroke="#fff" stroke-width="2"/></svg></span><span class="icon"><svg width="12" height="12"><path d="M6 11L1 5a3 3 0 0 1 5-3 3 3 0 0 1 5 3z" fill="#fff"/></svg></span><span class="price">£5.95</span></div></article>
  <article class="card"><div class="photo p-wind" role="img" aria-label="Light-up rainbow windmill"></div><h3>Rainbow Windmill</h3><p>Spinning windmill with bright rainbow lights for kids.</p><div class="card-foot"><span class="icon"><svg width="12" height="12"><path d="M1 6h10M6 1v10" stroke="#fff" stroke-width="2"/></svg></span><span class="icon"><svg width="12" height="12"><path d="M6 11L1 5a3 3 0 0 1 5-3 3 3 0 0 1 5 3z" fill="#fff"/></svg></span><span class="price">£3.95</span></div></article>
  <article class="card"><div class="photo p-foam" role="img" aria-label="Rainbow light-up foam stick"></div><h3>Rainbow Foam Stick</h3><p>Colour changing foam stick, great for events and discos.</p><div class="card-foot"><span class="icon"><svg width="12" height="12"><path d="M1 6h10M6 1v10" stroke="#fff" stroke-width="2"/></svg></span><span class="icon"><svg width="12" height="12"><path d="M6 11L1 5a3 3 0 0 1 5-3 3 3 0 0 1 5 3z" fill="#fff"/></svg></span><span class="price">£1.99</span></div></article>
</section>

<section class="products row-2">
  <article class="card"><div class="photo p-ring" role="img" aria-label="Flashing animal soft rings"></div><h3>Flashing Animal Soft Rings</h3><p>Soft light-up rings that flash in bright fun colours.</p><div class="card-foot"><span class="icon"><svg width="12" height="12"><path d="M1 6h10M6 1v10" stroke="#fff" stroke-width="2"/></svg></span><span class="icon"><svg width="12" height="12"><path d="M6 11L1 5a3 3 0 0 1 5-3 3 3 0 0 1 5 3z" fill="#fff"/></svg></span><span class="price">£0.89</span></div></article>
  <article class="card"><div class="photo p-cup" role="img" aria-label="Glowing party cups"></div><h3>Glow Cups</h3><p>Light-up cups that glow brightly at any school party.</p><div class="card-foot"><span class="icon"><svg width="12" height="12"><path d="M1 6h10M6 1v10" stroke="#fff" stroke-width="2"/></svg></span><span class="icon"><svg width="12" height="12"><path d="M6 11L1 5a3 3 0 0 1 5-3 3 3 0 0 1 5 3z" fill="#fff"/></svg></span><span class="price">£5.95</span></div></article>
  <article class="card"><div class="photo p-wind" role="img" aria-label="Light-up rainbow windmill"></div><h3>Rainbow Windmill</h3><p>Spinning windmill with bright rainbow lights for kids.</p><div class="card-foot"><span class="icon"><svg width="12" height="12"><path d="M1 6h10M6 1v10" stroke="#fff" stroke-width="2"/></svg></span><span class="icon"><svg width="12" height="12"><path d="M6 11L1 5a3 3 0 0 1 5-3 3 3 0 0 1 5 3z" fill="#fff"/></svg></span><span class="price">£3.95</span></div></article>
  <article class="card"><div class="photo p-foam" role="img" aria-label="Rainbow light-up foam stick"></div><h3>Rainbow Foam Stick</h3><p>Colour changing foam stick, great for events and discos.</p><div class="card-foot"><span class="icon"><svg width="12" height="12"><path d="M1 6h10M6 1v10" stroke="#fff" stroke-width="2"/></svg></span><span class="icon"><svg width="12" height="12"><path d="M6 11L1 5a3 3 0 0 1 5-3 3 3 0 0 1 5 3z" fill="#fff"/></svg></span><span class="price">£1.99</span></div></article>
</section>

<section class="perks">
  <div class="perk"><small>Original</small>Products</div>
  <div class="perk"><small>Free</small>Shipping</div>
  <div class="perk"><small>Cash On</small>Delivery</div>
  <div class="perk"><small>30 Days</small>Returns</div>
</section>

<section class="newsletter">
  <div class="label"><svg width="22" height="16" viewBox="0 0 22 16"><rect x="1" y="1" width="20" height="14" fill="none" stroke="#f78f20" stroke-width="2"/><path d="M1 1l10 8 10-8" fill="none" stroke="#f78f20" stroke-width="2"/></svg>Subscribe to our newsletter</div>
  <div class="field">Enter your email</div>
  <div class="btn">Subscribe Now</div>
  <div class="social">Stay connected <i></i><i></i><i></i><i></i><i></i></div>
</section>

<footer class="footer-cols">
  <div><h4>Information</h4><ul><li>About Us</li><li>Delivery Information</li><li>Privacy Policy</li><li>Terms &amp; Conditions</li><li>Blog</li></ul></div>
  <div><h4>Customer Service</h4><ul><li>Contact Us</li><li>Returns</li><li>Site Map</li><li>Brands</li></ul></div>
  <div><h4>My Account</h4><ul><li>My Account</li><li>Order History</li><li>Wish List</li><li>Newsletter</li></ul></div>
  <div><h4>We accept following payment methods</h4><div class="pay"><i></i><i></i><i></i><i></i><i></i></div></div>
</footer>

<div class="copyright">© 2024 ZIPPA things. All Rights Reserved.</div>

</body>
</html>
```